Dust N Gone! Cleaning needs a flyer!

We have started a cleaning business DUST N GONE! Cleaning, and had a new logo design for it.
We would like a flyer designed to present to businesses that represents our professionalism, quality of service, security and value for money.
We would like a flyer that we can present to both our residential clients and business owners alike.
We will use this flyer for the next 2 years without having to make changes.
I'm happy for the designer to come up with their own wording if necessary.
Updates

Hello everyone!

In addition to the information I have already provided, please see below for more information to be included on the design for our flyer.

Thank you in advance.

Don’t read this unless your current cleaners are AMAZING!

Are you still reading? Now for the good news! Announcing the arrival of the amazing cleaning team of Dust N Gone! Cleaning. They’re the BEST in the Wimmera and we personally guarantee it.

We offer an ultimate service that NO other cleaning company in the Wimmera can offer; high quality cleaning of your home or business, carpet dry cleaning and pest control. All of these services can be completed at a time that is most convenient to you.

From wiping benches to washing windows, from dusting skirting boards to dry cleaning your carpets, from bathrooms to bugs, we really are your ONE stop shop.

Why choose the greatest cleaning company in the Wimmera?

For over 18 years, we have built a reputation on honesty and trust in the residential and commercial services. Our business is to know what people expect when we walk in to your home or business.

With our vast experience and knowledge, we know how to find the best people for the job, how to identify the best products for the clean, we use the newest of technology and equipment and have the best attitudes in town.

Local people, local business that you can rely on because we are also Dust N Gone! Pest Control & Fibrelux all rolled in to your ONE stop shop for residential services.

Call us to discuss how we can give you the quality you demand.

Residential Cleaning                                                       Commercial Cleaning                                     

General house cleaning                                                  Business Premises          

Home help                                                                         Vacated properties

Rental vacancies                                                               Schools

Post renovation cleans                                                     Motels/Hotels

 

                                   

Target Market(s)

Business owners, commercial properties, home owners (women aged between 30 - 80y/o)

Industry/Entity Type

Residential

Requirements
Must have
• Incorporate our logo and colours.
Double sided.
Images of interiors of both home & office.
Catch phrase: "You demand quality ..... we guarantee it!"
Address: 22-26 Mallowdene St, Horsham VIC 3400
Phone: 1300 482 316
ABN: 47 385 602 139
We complete the ususal cleaning such as:
General House cleaning
Commercial Cleaning
Rental Properties
Business Premises
Other services we offer is:
Carpet dry cleaning
Upholstery cleaning
Dust N Gone! Critter Chasers pest control
Window cleaning.

```html
<!DOCTYPE html>
<html lang="en">
<head>
<meta charset="utf-8">
<title>Dust N Gone! Cleaning – Flyer</title>
<link rel="stylesheet" href="https://fonts.googleapis.com/css2?family=Jost:wght@400;500;700&family=Oswald:wght@700&family=Caveat:wght@400&display=swap">
<style>
  :root{
    --magenta:#b0509f;
    --magenta-light:#c770b5;
    --ink:#252123;
    --white:#ffffff;
    --grey-text:#bdb6ba;
    --stage-top:#ffffff;
    --stage-bottom:#d9d9d9;
    --label:#555555;
  }
  *{box-sizing:border-box;margin:0;padding:0}
  html,body{width:1200px;height:900px;overflow:hidden}
  body{
    position:relative;
    background:linear-gradient(180deg,var(--stage-top) 0%,var(--stage-top) 40%,var(--stage-bottom) 100%);
    font-family:"Jost",Arial,sans-serif;
    color:var(--white);
  }
  .side-label{
    position:absolute;font-family:"Jost",Arial,sans-serif;font-weight:700;
    font-size:16px;letter-spacing:.5px;color:var(--label);
  }
  .side-label--front{left:352px;top:100px}
  .side-label--back{left:770px;top:225px}

  .flyer{
    position:absolute;background:var(--ink);overflow:hidden;
    box-shadow:3px 4px 6px rgba(0,0,0,.35);
  }
  .flyer--front{left:352px;top:145px;width:360px;height:508px}
  .flyer--back{left:770px;top:268px;width:362px;height:512px}

  /* front */
  .front-art{position:absolute;left:0;top:0;width:360px;height:280px}
  .headline-banner{
    position:absolute;left:26px;top:244px;width:312px;height:48px;
    background:#1d1a1c;transform:rotate(-1.2deg);
    box-shadow:2px 3px 4px rgba(0,0,0,.45);
    padding:5px 0 0 12px;z-index:2;
  }
  .headline{font-family:"Oswald",Impact,sans-serif;font-weight:700;font-size:22px;line-height:24px;letter-spacing:.3px}
  .subhead{font-weight:700;font-size:11px;line-height:13px}
  .feature-band{
    position:absolute;left:0;top:275px;width:360px;height:185px;
    background:var(--magenta);padding:38px 16px 0 16px;
  }
  .lead-question{font-weight:700;font-size:12.5px;line-height:15px}
  .lead{font-size:14.5px;line-height:16.5px;margin-bottom:10px}
  .body-copy{font-size:10.5px;line-height:12.5px}

  .flyer-footer{position:absolute;left:0;bottom:0;width:100%;height:48px}
  .brand{
    position:absolute;left:14px;top:12px;font-weight:700;font-size:9px;line-height:10px;
    color:var(--white);display:flex;align-items:center;gap:4px;letter-spacing:.3px
  }
  .brand-mark{width:7px;height:7px;background:var(--magenta);flex:none}
  .brand-name{width:40px}
  .tagline{
    position:absolute;left:68px;top:2px;font-family:"Caveat",cursive;
    font-size:19px;letter-spacing:.6px;color:var(--magenta-light);white-space:nowrap
  }
  .contacts{position:absolute;left:84px;top:29px;font-size:8px;color:var(--grey-text);word-spacing:1px}
  .contacts b{color:var(--magenta);font-weight:500;margin-right:4px}
  .contacts span+span{margin-left:24px}

  /* back */
  .intro{position:absolute;left:18px;top:14px;width:325px;font-size:10.8px;line-height:21.5px}
  .intro strong{font-weight:700}
  .service-list{position:absolute;left:20px;top:99px;list-style:none}
  .service-list li{font-size:9px;line-height:14px;display:flex;align-items:center;gap:8px}
  .service-list li::before{content:"";width:6px;height:6px;background:var(--grey-text);flex:none}
  .office-art{position:absolute;left:160px;top:92px;width:202px;height:168px}
  .why-title{
    position:absolute;left:18px;top:258px;width:300px;font-weight:700;
    font-size:13px;line-height:22px;color:var(--magenta-light)
  }
  .why-copy{position:absolute;left:18px;top:313px;width:335px;font-size:8.6px;line-height:10.6px}
  .why-copy p{margin-bottom:12px}
  .why-copy strong{font-weight:700}
  .cta{font-weight:700;font-size:10.5px;line-height:12px}
  .flyer--back .flyer-footer{height:50px}
</style>
</head>
<body>

<div class="side-label side-label--front">FRONT</div>
<div class="side-label side-label--back">BACK</div>

<section class="flyer flyer--front">
  <svg class="front-art" viewBox="0 0 360 280" width="360" height="280">
    <defs>
      <linearGradient id="homeInterior" x1="0" y1="0" x2="0" y2="1">
        <stop offset="0" stop-color="#d8d6d2"/>
        <stop offset=".55" stop-color="#8a8570"/>
        <stop offset="1" stop-color="#4a3a2c"/>
      </linearGradient>
    </defs>
    <path role="img" aria-label="Photo of a bright home living room with sofa, armchair and kitchen"
          d="M0,150 L95,46 Q220,150 360,138 L360,280 L0,280 Z" fill="url(#homeInterior)"/>
    <path d="M0,124 L95,16 L138,38 L138,20 L152,20 L152,48 Q240,118 360,110 L360,138 Q220,150 95,46 L0,150 Z"
          fill="var(--magenta)"/>
  </svg>

  <div class="headline-banner">
    <h1 class="headline">DON’T READ THIS</h1>
    <p class="subhead">...unless your current cleaners are AMAZING!</p>
  </div>

  <div class="feature-band">
    <p class="lead-question">Are you still reading? Now for the good news!</p>
    <p class="lead">Announcing the arrival of the amazing cleaning team of Dust N Gone! Cleaning. They’re the BEST in the Wimmera and we personally guarantee it.</p>
    <p class="body-copy">We offer an ultimate service that NO other cleaning company in the Wimmera can offer; high quality cleaning of your home or business, carpet dry cleaning and pest control. All of these services can be completed at a time that is most convenient to you.</p>
  </div>

  <footer class="flyer-footer">
    <div class="brand"><span class="brand-mark"></span><span class="brand-name">DUST N GONE!</span></div>
    <div class="tagline">You demand quality ..... we guarantee it!</div>
    <div class="contacts"><span><b>P</b>1300 482 316</span><span><b>F</b>03 5391 6058</span></div>
  </footer>
</section>

<section class="flyer flyer--back">
  <p class="intro">From wiping benches to washing windows, from dusting skirting boards to dry cleaning your carpets, from bathrooms to bugs, we really are your <strong>ONE stop shop.</strong></p>

  <ul class="service-list">
    <li>Residential Cleaning</li>
    <li>Commercial Cleaning</li>
    <li>General house cleaning</li>
    <li>Business Premises</li>
    <li>Home help</li>
    <li>Vacated properties</li>
    <li>Rental vacancies</li>
    <li>Schools</li>
    <li>Post renovation cleans</li>
    <li>Motels/Hotels</li>
  </ul>

  <svg class="office-art" viewBox="0 0 202 168" width="202" height="168">
    <defs>
      <linearGradient id="officeInterior" x1="0" y1="0" x2="0" y2="1">
        <stop offset="0" stop-color="#e6e6e4"/>
        <stop offset=".6" stop-color="#a9a8a4"/>
        <stop offset="1" stop-color="#8a7456"/>
      </linearGradient>
    </defs>
    <polygon points="4,26 202,0 202,118 12,168" fill="var(--magenta)"/>
    <rect role="img" aria-label="Photo of a clean modern office meeting room" x="22" y="26" width="166" height="124" fill="url(#officeInterior)"/>
  </svg>

  <h2 class="why-title">Why choose the greatest cleaning company in the Wimmera?</h2>

  <div class="why-copy">
    <p>For over <strong>18 years</strong>, we have built a reputation on honesty and trust in the residential and commercial services. Our business is to know what people expect when we walk in to your home or business.</p>
    <p>With our vast experience and knowledge, we know how to find the best people for the job, how to identify the best products for the clean, we use the newest of technology and equipment and have the best attitudes in town.</p>
    <p>Local people, local business that you can rely on because we are also Dust N Gone! Pest Control &amp; Fibrelux all rolled in to your ONE stop shop for residential services.</p>
    <p class="cta">Call us to discuss how we can give you the quality you demand.</p>
  </div>

  <footer class="flyer-footer">
    <div class="brand"><span class="brand-mark"></span><span class="brand-name">DUST N GONE!</span></div>
    <div class="tagline">You demand quality ..... we guarantee it!</div>
    <div class="contacts"><span><b>P</b>1300 482 316</span><span><b>F</b>03 5391 6058</span></div>
  </footer>
</section>

</body>
</html>
```